Simple and clean webdesign for personal homepage

Trying to create a simple and clean webdesign for my personal homepage. Going to use a static site builder with templates to build the site. I want it to have multiple pages - like an about me, blog and resume. I just need something very basic I can customize. I want the main colors to be purple, black and white. I am open to other color palettes too but since purple is my favorite color I want that to be one of the main colors.

The site be mostly text driven. Might have some images in the body text but I want the site design to be light and lean.

Industry/Entity Type

Personal Homepage.

Coding

Coded - Design and coding required

Number of Pages Required

1 page

Font styles to use
Sans Serif

Colors
6B429C
8869AF
B7A5CE
E3DAEB
F3F0F8

Requirements
Must have
• Clean design. Purple used as a color. HTML template.
Nice to have
• Responsive

```html
<!DOCTYPE html>
<html lang="en">
<head>
<meta charset="utf-8">
<title>Daniel Carter — Personal Homepage</title>
<link href="https://fonts.googleapis.com/css2?family=Fira+Sans:wght@400;500;600;700&family=Roboto:wght@400;500;700&display=swap" rel="stylesheet">
<style>
:root{
  --stage:#808080;
  --purple-900:#4f2488;
  --purple-800:#5a2d8f;
  --purple-700:#6b429c;
  --purple-500:#7552a3;
  --lilac-300:#b7a5ce;
  --lilac-200:#dacfe8;
  --lilac-100:#e3daeb;
  --lavender-50:#f3f0f8;
  --ink:#1d1d22;
  --white:#ffffff;
  --head:"Fira Sans", sans-serif;
  --body:"Roboto", sans-serif;
}
*{margin:0;padding:0;box-sizing:border-box}
html,body{width:1200px;height:2627px;overflow:hidden;background:var(--stage)}
body{font-family:var(--body);color:var(--ink)}
.board{position:relative;width:1177px;height:2576px;transform:scale(1.0195);transform-origin:0 0}
.frame{position:absolute;top:42px;height:2495px;overflow:hidden;background:var(--white)}
.frame--desktop{left:23px;width:826px}
.frame--mobile{left:891px;width:197px}
.band{position:absolute;left:0;right:0}
.a{position:absolute}
.center{left:0;right:0;text-align:center}
.white{color:var(--white)}
.purple{color:var(--purple-700)}
.head{font-family:var(--head)}
.nowrap{white-space:nowrap}
.underline-bar{position:absolute;height:2px;background:currentColor}

/* hero */
.hero{background:linear-gradient(120deg,#5c2a99 0%,#5a3196 45%,#4e3a9c 100%)}
.hero__glow{position:absolute;inset:0;background:radial-gradient(ellipse 70% 90% at 25% 100%,rgba(120,70,190,.45),transparent 70%),radial-gradient(ellipse 60% 80% at 90% 0%,rgba(90,80,190,.5),transparent 70%)}
.brand{font-family:var(--head);font-weight:500;color:var(--white);white-space:nowrap}
.nav{display:flex;gap:17px;font-family:var(--head);font-size:12.5px;line-height:14px;color:var(--white);white-space:nowrap}
.btn-light{background:var(--white);color:var(--ink);border-radius:30px;font-family:var(--head);font-weight:500;text-align:center}
.btn-dark{background:var(--purple-800);color:var(--white);border-radius:30px;font-family:var(--head);font-weight:500;text-align:center}

/* about */
.about{background:linear-gradient(135deg,#efe8f8 0%,#fbf9fe 35%,#eee6f8 60%,#faf8fd 100%)}
.about__pattern{position:absolute;inset:0;background:linear-gradient(45deg,rgba(200,180,235,.25) 0%,transparent 40%,rgba(200,180,235,.3) 70%,transparent 100%)}
.portrait-ring{position:absolute;border-radius:50%;background:var(--lilac-100)}
.portrait{position:absolute;border-radius:50%;background:var(--purple-800);color:var(--white);text-align:center}

/* resume */
.section-title{font-family:var(--head);font-weight:500;color:var(--purple-700)}
.col-title{font-family:var(--head);font-weight:500;color:var(--ink);white-space:nowrap}
.entry{position:absolute;width:320px}
.frame--mobile .entry{width:176px}
.entry__year{position:absolute;left:0;top:0;border:2px solid var(--ink);border-radius:20px;font-family:var(--head);font-weight:600;text-align:center}
.entry__place{position:absolute;font-family:var(--head);color:var(--ink);white-space:nowrap}
.entry__role{position:absolute;font-family:var(--head);font-weight:500;color:var(--purple-700);white-space:nowrap}
.entry__text{position:absolute;font-weight:500;text-align:justify;color:var(--ink)}

/* portfolio */
.portfolio{background:var(--lilac-200)}
.arrow{position:absolute;border:1px solid var(--ink);display:flex;align-items:center;justify-content:center}
.photo{position:absolute;border-radius:14px}
.photo--office{background:linear-gradient(120deg,#8a5a3a 0%,#c58f62 35%,#6d86a8 70%,#3f5f86 100%)}
.photo--team{background:linear-gradient(120deg,#c9d6e8 0%,#7d97bf 35%,#3d5a8c 70%,#aebfd8 100%)}
.card-date{font-family:var(--head);color:var(--ink);white-space:nowrap}
.card-title{font-family:var(--head);font-weight:500;color:var(--purple-700)}

/* blog */
.post{position:absolute;background:var(--white);border:2px solid var(--lilac-100);box-shadow:0 2px 6px rgba(107,66,156,.18);display:flex;flex-direction:column}
.post__date{display:flex;align-items:center;color:#555;white-space:nowrap}
.post__title{font-family:var(--body);font-weight:400;color:var(--ink)}
.post__text{color:#555}
.post__more{margin-top:auto;font-family:var(--head);font-weight:500;color:var(--ink);text-decoration:underline}

/* contact */
.contact{background:var(--purple-500);color:var(--white)}
.contact__title{font-family:var(--head);font-weight:600;white-space:nowrap}
.contact__text{font-family:var(--body)}
.field{position:absolute;border:1px solid rgba(255,255,255,.8);font-family:var(--body);color:var(--white)}
.send{position:absolute;background:var(--purple-800);color:var(--white);border-radius:30px;font-family:var(--head);font-weight:600;text-align:center}

/* footer */
.footer{background:var(--purple-800);color:var(--white)}
.social{display:flex;font-family:var(--head);font-weight:600;white-space:nowrap}
</style>
</head>
<body>
<div class="board">

<!-- ================= DESKTOP ================= -->
<div class="frame frame--desktop">

  <header class="band hero" style="top:0;height:405px">
    <div class="hero__glow"></div>
    <div class="a brand" style="left:77px;top:20px;font-size:18px;line-height:22px">Daniel Carter</div>
    <nav class="a nav" style="right:77px;top:24px"><span>About Me</span><span>Resume</span><span>Portfolio</span><span>Blog</span><span>Contact</span></nav>
    <div class="a center white head" style="top:114px;font-size:15px;line-height:20px">Hello Its Me</div>
    <h1 class="a center white head" style="top:136px;font-size:55px;line-height:60px;font-weight:700">Daniel Carter</h1>
    <p class="a white" style="left:238px;width:350px;top:204px;font-size:11.5px;line-height:18px;text-align:center">Nemo enim ipsam voluptatem quia voluptas sit aspernatur aut odit aut fugit, sed quia consequuntur magni dolores eos qui ratione voluptatem sequi nesciunt.</p>
    <div class="a btn-light" style="left:365px;top:283px;width:96px;height:32px;line-height:32px;font-size:13px">Contact</div>
  </header>

  <section class="band about" style="top:405px;height:409px">
    <div class="about__pattern" role="img" aria-label="Soft lavender diagonal tile background"></div>
    <h2 class="a section-title" style="left:78px;top:88px;font-size:18px;line-height:22px">ABOUT ME</h2>
    <p class="a" style="left:80px;width:374px;top:132px;font-size:12.3px;line-height:18.7px;text-align:justify;color:#333">Lorem ipsum dolor sit amet, consectetur adipiscing elit, sed do eiusmod tempor incididunt ut labore et dolore magna aliqua. Ut enim ad minim veniam, quis nostrud exercitation ullamco laboris nisi ut aliquip ex ea commodo consequat. Duis aute irure dolor in reprehenderit in voluptate velit esse cillum dolore eu fugiat nulla pariatur. Excepteur sint occaecat cupidatat non proident, sunt in culpa qui officia deserunt mollit anim id est laborum."</p>
    <div class="a btn-dark" style="left:78px;top:285px;width:155px;height:33px;line-height:33px;font-size:12.5px">Download CV</div>
    <div class="portrait-ring" style="left:485px;top:54px;width:266px;height:266px"></div>
    <div class="portrait" style="left:502px;top:71px;width:232px;height:232px">
      <div class="a center head" style="top:95px;font-size:14px;line-height:18px">Hello Its Me</div>
      <div class="a center head" style="top:114px;font-size:28px;line-height:34px;font-weight:600">Daniel Carter</div>
    </div>
  </section>

  <section class="band resume" style="top:814px;height:564px">
    <h2 class="a section-title center" style="top:40px;font-size:22px;line-height:26px">Resume</h2>
    <div class="underline-bar purple" style="left:373px;width:80px;top:66px"></div>

    <h3 class="a col-title" style="left:75px;top:90px;font-size:18px;line-height:22px">Education</h3>
    <div class="underline-bar" style="left:75px;width:83px;top:112px;color:var(--ink)"></div>
    <h3 class="a col-title" style="left:439px;top:90px;font-size:18px;line-height:22px">Experience</h3>
    <div class="underline-bar" style="left:439px;width:93px;top:112px;color:var(--ink)"></div>

    <div class="entry" style="left:76px;top:131px">
      <div class="entry__year" style="width:70px;height:26px;line-height:22px;font-size:15px">2009</div>
      <div class="entry__place" style="left:75px;top:5px;font-size:12.5px;line-height:16px">University of Studies</div>
      <div class="entry__role" style="left:21px;top:37px;font-size:19px;line-height:24px">UI Design</div>
      <p class="entry__text" style="left:23px;width:283px;top:68px;font-size:10.8px;line-height:15.5px">Duis posuere, quam non imperdiet egestas, eros enim mattis mauris, in posuere lacus arcu quis felis. Etiam interdum erat non enim venenatis fermentum.</p>
    </div>
    <div class="entry" style="left:76px;top:268px">
      <div class="entry__year" style="width:70px;height:26px;line-height:22px;font-size:15px">2008</div>
      <div class="entry__place" style="left:75px;top:5px;font-size:12.5px;line-height:16px">University of Studies</div>
      <div class="entry__role" style="left:21px;top:37px;font-size:19px;line-height:24px">Graphic Design</div>
      <p class="entry__text" style="left:23px;width:283px;top:68px;font-size:10.8px;line-height:15.5px">Duis posuere, quam non imperdiet egestas, eros enim mattis mauris, in posuere lacus arcu quis felis. Etiam interdum erat non enim venenatis fermentum.</p>
    </div>
    <div class="entry" style="left:76px;top:413px">
      <div class="entry__year" style="width:70px;height:26px;line-height:22px;font-size:15px">2007</div>
      <div class="entry__place" style="left:75px;top:5px;font-size:12.5px;line-height:16px">University of Studies</div>
      <div class="entry__role" style="left:21px;top:37px;font-size:19px;line-height:24px">Frontend Development</div>
      <p class="entry__text" style="left:23px;width:283px;top:68px;font-size:10.8px;line-height:15.5px">Duis posuere, quam non imperdiet egestas, eros enim mattis mauris, in posuere lacus arcu quis felis. Etiam interdum erat non enim venenatis fermentum.</p>
    </div>

    <div class="entry" style="left:440px;top:131px">
      <div class="entry__year" style="width:70px;height:26px;line-height:22px;font-size:15px">2010</div>
      <div class="entry__place" style="left:75px;top:5px;font-size:12.5px;line-height:16px">Northwind Studio</div>
      <div class="entry__role" style="left:21px;top:37px;font-size:19px;line-height:24px">Lead UI/UX Designer</div>
      <p class="entry__text" style="left:23px;width:283px;top:68px;font-size:10.8px;line-height:15.5px">Duis posuere, quam non imperdiet egestas, eros enim mattis mauris, in posuere lacus arcu quis felis. Etiam interdum erat non enim venenatis fermentum.</p>
    </div>
    <div class="entry" style="left:440px;top:268px">
      <div class="entry__year" style="width:70px;height:26px;line-height:22px;font-size:15px">2015</div>
      <div class="entry__place" style="left:75px;top:5px;font-size:12.5px;line-height:16px">Brightleaf Goods</div>
      <div class="entry__role" style="left:21px;top:37px;font-size:19px;line-height:24px">Senior UI/UX Designer</div>
      <p class="entry__text" style="left:23px;width:283px;top:68px;font-size:10.8px;line-height:15.5px">Duis posuere, quam non imperdiet egestas, eros enim mattis mauris, in posuere lacus arcu quis felis. Etiam interdum erat non enim venenatis fermentum.</p>
    </div>
    <div class="entry" style="left:440px;top:413px">
      <div class="entry__year" style="width:70px;height:26px;line-height:22px;font-size:15px">2022</div>
      <div class="entry__place" style="left:75px;top:5px;font-size:12.5px;line-height:16px">Cedar Lane</div>
      <div class="entry__role" style="left:21px;top:37px;font-size:19px;line-height:24px">Junior UI/UX Designer</div>
      <p class="entry__text" style="left:23px;width:283px;top:68px;font-size:10.8px;line-height:15.5px">Duis posuere, quam non imperdiet egestas, eros enim mattis mauris, in posuere lacus arcu quis felis. Etiam interdum erat non enim venenatis fermentum.</p>
    </div>
  </section>

  <section class="band portfolio" style="top:1378px;height:373px">
    <h2 class="a col-title" style="left:81px;top:20px;font-size:18px;line-height:22px">Portfolio</h2>
    <div class="underline-bar" style="left:81px;width:70px;top:44px;color:var(--ink)"></div>
    <div class="arrow" style="left:698px;top:24px;width:20px;height:20px"><svg width="8" height="10" viewBox="0 0 8 10"><path d="M6 1 2 5l4 4" fill="none" stroke="#1d1d22" stroke-width="1.3"/></svg></div>
    <div class="arrow" style="left:727px;top:24px;width:20px;height:20px"><svg width="8" height="10" viewBox="0 0 8 10"><path d="M2 1l4 4-4 4" fill="none" stroke="#1d1d22" stroke-width="1.3"/></svg></div>

    <div class="photo photo--office" role="img" aria-label="Photo of two colleagues looking at a tablet in an office" style="left:76px;top:77px;width:324px;height:196px"></div>
    <div class="a card-date" style="left:76px;top:280px;font-size:12px;line-height:16px">05 Jan2022</div>
    <div class="a card-title nowrap" style="left:75px;top:298px;font-size:16px;line-height:20px">Creative and Innovative Navigation Designs</div>

    <div class="photo photo--team" role="img" aria-label="Photo of a team gathered around a laptop and tablet" style="left:422px;top:77px;width:323px;height:196px"></div>
    <div class="a card-date" style="left:422px;top:280px;font-size:12px;line-height:16px">05 Jan2022</div>
    <div class="a card-title nowrap" style="left:421px;top:298px;font-size:16px;line-height:20px">Creative and Innovative Navigation Designs</div>
  </section>

  <section class="band blog" style="top:1751px;height:364px">
    <h2 class="a section-title center" style="top:55px;font-size:19px;line-height:24px">Latest Blog</h2>
    <p class="a center" style="top:86px;font-size:11px;line-height:14px;color:#333">Sed ut perspiciatis unde omnis iste natus error sit voluptatem</p>

    <article class="post" style="left:76px;top:139px;width:213px;height:175px;padding:17px 6px 17px 11px">
      <div class="post__date" style="font-size:10px;line-height:14px;gap:9px"><svg width="10" height="10" viewBox="0 0 10 10"><circle cx="5" cy="5" r="4" fill="none" stroke="#6b429c" stroke-width="1.4"/><path d="M5 3v2h1.6" stroke="#6b429c" stroke-width="1.2" fill="none"/></svg>January 12,2022</div>
      <h3 class="post__title" style="margin-top:10px;font-size:14px;line-height:19px">Sed ut perspiciatis unde omnis iste natus error sit voluptatem</h3>
      <p class="post__text" style="margin-top:10px;font-size:10.3px;line-height:18px">Lorem ipsum dolor sit amet, consectetur adipiscing elit, sed do eiusmod tempor</p>
      <div class="post__more" style="font-size:10.5px;line-height:14px">Learn More</div>
    </article>
    <article class="post" style="left:305px;top:139px;width:213px;height:175px;padding:17px 6px 17px 11px">
      <div class="post__date" style="font-size:10px;line-height:14px;gap:9px"><svg width="10" height="10" viewBox="0 0 10 10"><circle cx="5" cy="5" r="4" fill="none" stroke="#6b429c" stroke-width="1.4"/><path d="M5 3v2h1.6" stroke="#6b429c" stroke-width="1.2" fill="none"/></svg>January12,2022</div>
      <h3 class="post__title" style="margin-top:10px;font-size:14px;line-height:19px">Sed ut perspiciatis unde omnis iste natus error sit voluptatem</h3>
      <p class="post__text" style="margin-top:10px;font-size:10.3px;line-height:18px">Lorem ipsum dolor sit amet, consectetur adipiscing elit, sed do eiusmod tempor</p>
      <div class="post__more" style="font-size:10.5px;line-height:14px">Learn More</div>
    </article>
    <article class="post" style="left:533px;top:139px;width:213px;height:175px;padding:17px 6px 17px 11px">
      <div class="post__date" style="font-size:10px;line-height:14px;gap:9px"><svg width="10" height="10" viewBox="0 0 10 10"><circle cx="5" cy="5" r="4" fill="none" stroke="#6b429c" stroke-width="1.4"/><path d="M5 3v2h1.6" stroke="#6b429c" stroke-width="1.2" fill="none"/></svg>January 12,2022</div>
      <h3 class="post__title" style="margin-top:10px;font-size:14px;line-height:19px">Sed ut perspiciatis unde omnis iste natus error sit voluptatem</h3>
      <p class="post__text" style="margin-top:10px;font-size:10.3px;line-height:18px">Lorem ipsum dolor sit amet, consectetur adipiscing elit, sed do eiusmod tempor</p>
      <div class="post__more" style="font-size:10.5px;line-height:14px">Learn More</div>
    </article>
  </section>

  <section class="band contact" style="top:2115px;height:313px">
    <svg class="a" style="left:75px;top:45px" width="20" height="20" viewBox="0 0 24 24"><path d="M6.6 10.8c1.4 2.8 3.8 5.1 6.6 6.6l2.2-2.2c.3-.3.7-.4 1-.2 1.1.4 2.3.6 3.6.6.6 0 1 .4 1 1V20c0 .6-.4 1-1 1C10.6 21 3 13.4 3 4c0-.6.4-1 1-1h3.5c.6 0 1 .4 1 1 0 1.3.2 2.5.6 3.6.1.3 0 .7-.2 1z" fill="#fff"/></svg>
    <div class="a contact__title" style="left:110px;top:37px;font-size:14.5px;line-height:20px">415-555-0148</div>
    <p class="a contact__text" style="left:110px;width:260px;top:59px;font-size:14.5px;line-height:21px">Duis erat leo, aliquam laoreet fringilla quis, pretium vitae dui.</p>

    <svg class="a" style="left:77px;top:124px" width="16" height="20" viewBox="0 0 16 20"><path d="M8 1a6 6 0 0 0-6 6c0 4.5 6 11.5 6 11.5S14 11.5 14 7a6 6 0 0 0-6-6z" fill="none" stroke="#fff" stroke-width="2"/><circle cx="8" cy="7" r="2" fill="#fff"/></svg>
    <div class="a contact__title" style="left:110px;top:119px;font-size:14.5px;line-height:20px">Lorem ipsum</div>
    <p class="a contact__text" style="left:110px;width:260px;top:141px;font-size:14.5px;line-height:21px">Duis erat leo, aliquam laoreet fringilla quis, pretium vitae dui.</p>

    <svg class="a" style="left:75px;top:210px" width="21" height="16" viewBox="0 0 21 16"><rect x="1" y="1" width="19" height="14" rx="1.5" fill="none" stroke="#fff" stroke-width="1.8"/><path d="M1.5 2l9 7 9-7" fill="none" stroke="#fff" stroke-width="1.8"/></svg>
    <div class="a contact__title" style="left:110px;top:205px;font-size:14.5px;line-height:20px">hello@violetdesk.com</div>
    <p class="a contact__text" style="left:110px;width:260px;top:227px;font-size:14.5px;line-height:21px">Duis erat leo, aliquam laoreet fringilla quis, pretium vitae dui.</p>

    <h2 class="a head nowrap" style="left:382px;top:35px;font-size:18.5px;line-height:24px;font-weight:500">How Can I Help You?</h2>
    <div class="field" style="left:384px;top:72px;width:176px;height:36px;padding:13px 10px;font-size:9px">Name</div>
    <div class="field" style="left:570px;top:72px;width:176px;height:36px;padding:13px 10px;font-size:9px">Phone</div>
    <div class="field" style="left:384px;top:117px;width:362px;height:36px;padding:13px 10px;font-size:9px">Email Adrees</div>
    <div class="field" style="left:384px;top:161px;width:362px;height:68px;padding:10px 10px;font-size:9px">Message</div>
    <div class="send" style="left:514px;top:242px;width:102px;height:31px;line-height:31px;font-size:11px">SEND</div>
  </section>

  <footer class="band footer" style="top:2428px;height:67px">
    <div class="a social" style="left:77px;top:26px;gap:17px;font-size:11.5px;line-height:14px"><span>Microblog</span><span>Friendbook</span><span>Photoreel</span></div>
    <div class="a head nowrap" style="right:79px;top:24px;font-size:11.5px;line-height:14px;font-weight:600">© copyrights 2022 Daniel Carter |&nbsp; All Rights Reserved</div>
  </footer>
</div>

<!-- ================= MOBILE ================= -->
<div class="frame frame--mobile">

  <header class="band hero" style="top:0;height:122px">
    <div class="hero__glow"></div>
    <div class="a brand" style="left:12px;top:7px;font-size:9.5px;line-height:12px">Daniel Carter</div>
    <svg class="a" style="left:176px;top:9px" width="10" height="8" viewBox="0 0 10 8"><path d="M0 1h10M0 4h10M0 7h10" stroke="#fff" stroke-width="1.3"/></svg>
    <div class="a center white head" style="top:34px;font-size:8.5px;line-height:10px">Hello Its Me</div>
    <div class="a center white head" style="top:45px;font-size:15px;line-height:18px;font-weight:600">Daniel Carter</div>
    <p class="a white" style="left:28px;width:141px;top:67px;font-size:5.3px;line-height:9px;text-align:center">Nemo enim ipsam voluptatem quia voluptas sit aspernatur aut odit aut fugit, sed quia</p>
    <div class="a btn-light" style="left:71px;top:94px;width:51px;height:17px;line-height:17px;font-size:5.5px">Contact</div>
  </header>

  <section class="band about" style="top:122px;height:346px">
    <div class="about__pattern" role="img" aria-label="Soft lavender diagonal tile background"></div>
    <div class="portrait-ring" style="left:35px;top:23px;width:128px;height:128px"></div>
    <div class="portrait" style="left:42px;top:30px;width:114px;height:114px">
      <div class="a center head" style="top:35px;font-size:8.5px;line-height:10px">Hello Its Me</div>
      <div class="a center head" style="top:50px;font-size:13px;line-height:16px;font-weight:600">Daniel Carter</div>
    </div>
    <h2 class="a section-title center" style="top:169px;font-size:15px;line-height:18px">ABOUT ME</h2>
    <p class="a" style="left:11px;width:176px;top:197px;font-size:10px;line-height:15.7px;text-align:justify;color:#333">Lorem ipsum dolor sit adipiscing eli sed do eiusmod tempor incididunt ut labore et dolore magna aliqua. Ut enim ad minim veniam</p>
    <div class="a btn-dark" style="left:28px;top:301px;width:130px;height:28px;line-height:28px;font-size:9.5px">Download CV</div>
  </section>

  <section class="band resume" style="top:468px;height:616px">
    <h2 class="a section-title center" style="top:15px;font-size:10px;line-height:13px">Resume</h2>
    <div class="underline-bar purple" style="left:79px;width:39px;top:29px;height:1px"></div>
    <h3 class="a col-title" style="left:12px;top:37px;font-size:12px;line-height:15px">Education</h3>
    <div class="underline-bar" style="left:12px;width:62px;top:52px;height:1.5px;color:var(--ink)"></div>

    <div class="entry" style="left:12px;top:64px">
      <div class="entry__year" style="width:57px;height:18px;line-height:15px;font-size:9px;border-width:1.5px">2009</div>
      <div class="entry__place" style="left:67px;top:3px;font-size:8.5px;line-height:12px">University of Studies</div>
      <div class="entry__role" style="left:0;top:28px;font-size:12.5px;line-height:16px">UI Design</div>
      <p class="entry__text" style="left:0;width:174px;top:48px;font-size:7.3px;line-height:13px;font-weight:400">Duis posuere, quam non imperdiet eros enim mattis mauris, in posuere lacus arcu quis feli.</p>
    </div>
    <div class="entry" style="left:12px;top:149px">
      <div class="entry__year" style="width:57px;height:18px;line-height:15px;font-size:9px;border-width:1.5px">2008</div>
      <div class="entry__place" style="left:67px;top:3px;font-size:8.5px;line-height:12px">University of Studies</div>
      <div class="entry__role" style="left:0;top:28px;font-size:12.5px;line-height:16px">Graphic Design</div>
      <p class="entry__text" style="left:0;width:174px;top:48px;font-size:7.3px;line-height:13px;font-weight:400">Duis posuere, quam non imperdiet eros enim mattis mauris, in posuere lacus arcu quis feli.</p>
    </div>
    <div class="entry" style="left:12px;top:235px">
      <div class="entry__year" style="width:57px;height:18px;line-height:15px;font-size:9px;border-width:1.5px">2007</div>
      <div class="entry__place" style="left:67px;top:3px;font-size:8.5px;line-height:12px">University of Studies</div>
      <div class="entry__role" style="left:0;top:28px;font-size:12.5px;line-height:16px">Frontend Development</div>
      <p class="entry__text" style="left:0;width:174px;top:48px;font-size:7.3px;line-height:13px;font-weight:400">Duis posuere, quam non imperdiet eros enim mattis mauris, in posuere lacus arcu quis feli.</p>
    </div>

    <h3 class="a col-title" style="left:12px;top:330px;font-size:12px;line-height:15px">Experience</h3>
    <div class="underline-bar" style="left:12px;width:68px;top:345px;height:1.5px;color:var(--ink)"></div>

    <div class="entry" style="left:12px;top:357px">
      <div class="entry__year" style="width:57px;height:18px;line-height:15px;font-size:9px;border-width:1.5px">2010</div>
      <div class="entry__place" style="left:67px;top:3px;font-size:8.5px;line-height:12px">Northwind Studio</div>
      <div class="entry__role" style="left:0;top:28px;font-size:12.5px;line-height:16px">Lead UI/UX Designer</div>
      <p class="entry__text" style="left:0;width:174px;top:48px;font-size:7.3px;line-height:13px;font-weight:400">Duis posuere, quam non imperdiet eros enim mattis mauris, in posuere lacus arcu quis feli.</p>
    </div>
    <div class="entry" style="left:12px;top:442px">
      <div class="entry__year" style="width:57px;height:18px;line-height:15px;font-size:9px;border-width:1.5px">2015</div>
      <div class="entry__place" style="left:67px;top:3px;font-size:8.5px;line-height:12px">Brightleaf Goods</div>
      <div class="entry__role" style="left:0;top:28px;font-size:12.5px;line-height:16px">Senior UI/UX Designer</div>
      <p class="entry__text" style="left:0;width:174px;top:48px;font-size:7.3px;line-height:13px;font-weight:400">Duis posuere, quam non imperdiet eros enim mattis mauris, in posuere lacus arcu quis feli.</p>
    </div>
    <div class="entry" style="left:12px;top:528px">
      <div class="entry__year" style="width:57px;height:18px;line-height:15px;font-size:9px;border-width:1.5px">2022</div>
      <div class="entry__place" style="left:67px;top:3px;font-size:8.5px;line-height:12px">Cedar Lane</div>
      <div class="entry__role" style="left:0;top:28px;font-size:12.5px;line-height:16px">Junior UI/UX Designer</div>
      <p class="entry__text" style="left:0;width:174px;top:48px;font-size:7.3px;line-height:13px;font-weight:400">Duis posuere, quam non imperdiet eros enim mattis mauris, in posuere lacus arcu quis feli.</p>
    </div>
  </section>

  <section class="band portfolio" style="top:1084px;height:208px">
    <h2 class="a col-title" style="left:11px;top:10px;font-size:12px;line-height:15px">Portfolio</h2>
    <div class="underline-bar" style="left:11px;width:30px;top:27px;height:1.5px;color:var(--ink)"></div>
    <div class="arrow" style="left:153px;top:11px;width:13px;height:13px"><svg width="5" height="7" viewBox="0 0 5 7"><path d="M4 .5 1 3.5l3 3" fill="none" stroke="#1d1d22"/></svg></div>
    <div class="arrow" style="left:172px;top:11px;width:13px;height:13px"><svg width="5" height="7" viewBox="0 0 5 7"><path d="M1 .5l3 3-3 3" fill="none" stroke="#1d1d22"/></svg></div>
    <div class="photo photo--office" role="img" aria-label="Photo of two colleagues looking at a tablet in an office" style="left:12px;top:44px;width:174px;height:92px;border-radius:6px"></div>
    <div class="a card-date" style="left:12px;top:144px;font-size:8px;line-height:11px">05 Jan2022</div>
    <div class="a card-title" style="left:12px;width:160px;top:157px;font-size:10px;line-height:16px">Creative and Innovative Navigation Designs</div>
  </section>

  <section class="band blog" style="top:1292px;height:551px">
    <h2 class="a section-title" style="left:13px;top:14px;font-size:12px;line-height:15px">Latest Blog</h2>
    <p class="a" style="left:12px;width:178px;top:42px;font-size:7.8px;line-height:16px;color:#333">Sed ut perspiciatis unde omnis iste Natu naturror sit voluptatem</p>

    <article class="post" style="left:12px;top:82px;width:174px;height:136px;padding:14px 5px 12px 9px">
      <div class="post__date" style="font-size:6px;line-height:10px;gap:7px"><svg width="7" height="7" viewBox="0 0 10 10"><circle cx="5" cy="5" r="4" fill="none" stroke="#6b429c" stroke-width="1.6"/><path d="M5 3v2h1.6" stroke="#6b429c" stroke-width="1.4" fill="none"/></svg>January 12,2022</div>
      <h3 class="post__title" style="margin-top:8px;font-size:10px;line-height:14.5px">Sed ut perspiciatis unde omnis iste natus error sit voluptatem</h3>
      <p class="post__text" style="margin-top:7px;font-size:6.6px;line-height:14px">Lorem ipsum dolor sit amet, consectetur adipiscing elit, sed do eiusmod tempor</p>
      <div class="post__more" style="font-size:6.5px;line-height:10px">Learn More</div>
    </article>
    <article class="post" style="left:12px;top:236px;width:174px;height:135px;padding:14px 5px 12px 9px">
      <div class="post__date" style="font-size:6px;line-height:10px;gap:7px"><svg width="7" height="7" viewBox="0 0 10 10"><circle cx="5" cy="5" r="4" fill="none" stroke="#6b429c" stroke-width="1.6"/><path d="M5 3v2h1.6" stroke="#6b429c" stroke-width="1.4" fill="none"/></svg>January 12,2022</div>
      <h3 class="post__title" style="margin-top:8px;font-size:10px;line-height:14.5px">Sed ut perspiciatis unde omnis iste natus error sit voluptatem</h3>
      <p class="post__text" style="margin-top:7px;font-size:6.6px;line-height:14px">Lorem ipsum dolor sit amet, consectetur adipiscing elit, sed do eiusmod tempor</p>
      <div class="post__more" style="font-size:6.5px;line-height:10px">Learn More</div>
    </article>
    <article class="post" style="left:12px;top:389px;width:174px;height:135px;padding:14px 5px 12px 9px">
      <div class="post__date" style="font-size:6px;line-height:10px;gap:7px"><svg width="7" height="7" viewBox="0 0 10 10"><circle cx="5" cy="5" r="4" fill="none" stroke="#6b429c" stroke-width="1.6"/><path d="M5 3v2h1.6" stroke="#6b429c" stroke-width="1.4" fill="none"/></svg>January 12,2022</div>
      <h3 class="post__title" style="margin-top:8px;font-size:10px;line-height:14.5px">Sed ut perspiciatis unde omnis iste natus error sit voluptatem</h3>
      <p class="post__text" style="margin-top:7px;font-size:6.6px;line-height:14px">Lorem ipsum dolor sit amet, consectetur adipiscing elit, sed do eiusmod tempor</p>
      <div class="post__more" style="font-size:6.5px;line-height:10px">Learn More</div>
    </article>
  </section>

  <section class="band contact" style="top:1843px;height:563px">
    <svg class="a" style="left:86px;top:12px" width="25" height="25" viewBox="0 0 25 25"><circle cx="12.5" cy="12.5" r="11.5" fill="none" stroke="#fff" stroke-width="1.3"/><path d="M9.6 11.6c.8 1.6 2.2 3 3.8 3.8l1.3-1.3c.2-.2.4-.2.6-.1.6.2 1.3.3 2 .3.3 0 .6.2.6.6v2c0 .3-.3.6-.6.6-5.4 0-9.8-4.4-9.8-9.8 0-.3.3-.6.6-.6h2c.3 0 .6.3.6.6 0 .7.1 1.4.3 2 .1.2 0 .4-.1.6z" fill="#fff"/></svg>
    <div class="a center head" style="top:40px;font-size:8.5px;line-height:12px;font-weight:600">+1 415-555-0148</div>
    <p class="a" style="left:12px;width:174px;top:57px;font-size:8.5px;line-height:16px;text-align:justify">Duis erat leo, aliquam laoreet fringilla quis, pretium vitae dui.</p>

    <svg class="a" style="left:86px;top:102px" width="25" height="25" viewBox="0 0 25 25"><circle cx="12.5" cy="12.5" r="11.5" fill="none" stroke="#fff" stroke-width="1.3"/><path d="M12.5 6.5a4 4 0 0 0-4 4c0 3 4 7.5 4 7.5s4-4.5 4-7.5a4 4 0 0 0-4-4z" fill="none" stroke="#fff" stroke-width="1.3"/><circle cx="12.5" cy="10.5" r="1.3" fill="#fff"/></svg>
    <div class="a center head" style="top:130px;font-size:8.5px;line-height:12px;font-weight:600">Location</div>
    <p class="a" style="left:12px;width:174px;top:147px;font-size:8.5px;line-height:16px;text-align:justify">Duis erat leo, aliquam laoreet fringilla quis, pretium vitae dui.</p>

    <svg class="a" style="left:86px;top:194px" width="25" height="25" viewBox="0 0 25 25"><circle cx="12.5" cy="12.5" r="11.5" fill="none" stroke="#fff" stroke-width="1.3"/><path d="M9.6 11.6c.8 1.6 2.2 3 3.8 3.8l1.3-1.3c.2-.2.4-.2.6-.1.6.2 1.3.3 2 .3.3 0 .6.2.6.6v2c0 .3-.3.6-.6.6-5.4 0-9.8-4.4-9.8-9.8 0-.3.3-.6.6-.6h2c.3 0 .6.3.6.6 0 .7.1 1.4.3 2 .1.2 0 .4-.1.6z" fill="#fff"/></svg>
    <div class="a center head" style="top:222px;font-size:8.5px;line-height:12px;font-weight:600">info@danielcarter.com</div>
    <p class="a" style="left:12px;width:174px;top:239px;font-size:8.5px;line-height:16px;text-align:justify">Duis erat leo, aliquam laoreet fringilla quis, pretium vitae dui.</p>

    <h2 class="a center head" style="top:292px;font-size:14.5px;line-height:18px;font-weight:500">How Can I Help You?</h2>
    <div class="field" style="left:20px;top:329px;width:158px;height:30px;padding:11px 8px;font-size:6.5px">Name</div>
    <div class="field" style="left:20px;top:364px;width:158px;height:30px;padding:11px 8px;font-size:6.5px">Phone</div>
    <div class="field" style="left:20px;top:398px;width:158px;height:30px;padding:11px 8px;font-size:6.5px">Email Adrees</div>
    <div class="field" style="left:20px;top:432px;width:158px;height:73px;padding:9px 8px;font-size:6.5px">Message</div>
    <div class="send" style="left:62px;top:520px;width:63px;height:23px;line-height:23px;font-size:7.5px">SEND</div>
  </section>

  <footer class="band footer" style="top:2406px;height:89px">
    <div class="a social" style="left:25px;top:18px;gap:14px;font-size:8.3px;line-height:11px"><span>Microblog</span><span style="text-decoration:underline">Friendbook</span><span>Photoreel</span></div>
    <div class="a center" style="top:44px;font-size:5.3px;line-height:7px">© copyrights 2022 Daniel Carter | &nbsp;All Rights Reserved</div>
  </footer>
</div>

</div>
</body>
</html>
```